Scrap Metal Recycling

We are looking for a simple yet bold business card. We already have the logo, please see attached. Color scheme of blue, black and white or just blue and white.

```html
<!DOCTYPE html>
<html lang="en">
<head>
<meta charset="utf-8">
<title>Ridgeline Metals Inc. – Business Card</title>
<link href="https://fonts.googleapis.com/css2?family=Inter:wght@400;500;600;700&family=Saira:wght@600&display=swap" rel="stylesheet">
<style>
  :root {
    --backdrop: #2b2b2c;
    --card: #232425;
    --card-edge: #2c2d2f;
    --emboss: #161617;
    --blue: #0f86a4;
    --white: #f2f2f2;
    --muted: #d9d9d9;
  }
  * { margin: 0; padding: 0; box-sizing: border-box; }
  html, body { width: 1200px; height: 1138px; overflow: hidden; }
  body {
    background: var(--backdrop);
    font-family: "Inter", Arial, sans-serif;
    position: relative;
  }
  .card {
    position: absolute;
    left: 290px;
    width: 620px;
    height: 375px;
    border-radius: 18px;
    background: linear-gradient(160deg, var(--card) 0%, var(--card-edge) 100%);
    overflow: hidden;
  }
  .card-front { top: 186px; }
  .card-back { top: 608px; }

  /* front */
  .front-lockup {
    position: absolute;
    top: 148px; left: 0; right: 0;
    text-align: center;
  }
  .front-lockup .company-name {
    font-weight: 700;
    font-size: 42px;
    color: var(--emboss);
    letter-spacing: -0.5px;
  }
  .front-lockup .tagline {
    margin-top: 4px;
    font-weight: 600;
    font-size: 22px;
    letter-spacing: 7px;
    color: var(--emboss);
  }
  .front-web {
    position: absolute;
    top: 324px; left: 0; right: 0;
    text-align: center;
    font-size: 15px;
    color: var(--muted);
  }
  .front-web .domain { color: var(--blue); }

  /* back */
  .back-lockup { position: absolute; left: 34px; top: 60px; }
  .back-lockup .company-name {
    font-weight: 700;
    font-size: 40px;
    color: var(--white);
    letter-spacing: -0.5px;
  }
  .back-lockup .tagline {
    margin-top: 2px;
    font-weight: 600;
    font-size: 23px;
    letter-spacing: 7.2px;
    color: var(--blue);
  }
  .person { position: absolute; left: 34px; top: 200px; }
  .person .name {
    font-family: "Saira", Arial, sans-serif;
    font-weight: 600;
    font-size: 24px;
    color: var(--blue);
    line-height: 1.1;
  }
  .person .role { margin-top: 6px; font-size: 16px; color: var(--muted); }
  .address {
    position: absolute; left: 34px; top: 292px;
    font-size: 16px; line-height: 23px; color: var(--muted);
  }
  .contacts {
    position: absolute; left: 322px; top: 203px;
    list-style: none;
  }
  .contacts li {
    display: flex; align-items: center; gap: 12px;
    height: 22.5px;
    font-size: 16px; color: var(--muted);
  }
  .contacts svg { width: 15px; height: 15px; fill: var(--blue); }
  .footer-band {
    position: absolute; right: 0; bottom: 0;
    width: 364px; height: 45px;
    background: var(--blue);
    clip-path: polygon(20px 0, 100% 0, 100% 100%, 0 100%);
    display: flex; align-items: center; justify-content: center;
    padding-left: 14px;
    font-weight: 700; font-size: 16px; color: var(--white);
  }
</style>
</head>
<body>

<section class="card card-front">
  <div class="front-lockup">
    <div class="company-name">RIDGELINE METALS INC.</div>
    <div class="tagline">SCRAP METAL RECYCLING</div>
  </div>
  <div class="front-web">www.<span class="domain">yourwebsite</span>.com</div>
</section>

<section class="card card-back">
  <div class="back-lockup">
    <div class="company-name">RIDGELINE METALS INC.</div>
    <div class="tagline">SCRAP METAL RECYCLING</div>
  </div>

  <div class="person">
    <div class="name">DANA WHITFIELD</div>
    <div class="role">Managing Director</div>
  </div>

  <div class="address">234 Anywhere St.,<br>Any Town, US 123456</div>

  <ul class="contacts">
    <li>
      <svg viewBox="0 0 16 16" aria-hidden="true"><path d="M2 5c0-2 2.5-3 6-3s6 1 6 3v1.5h-3V5H5v1.5H2z"/><path d="M3 8h10l1 6H2z"/></svg>
      000-111-1111
    </li>
    <li>
      <svg viewBox="0 0 16 16" aria-hidden="true"><path d="M1 3h14v10H1z M2.5 4.5 8 9l5.5-4.5" /><path d="M1 3h14L8 8.5z" fill="#1a1b1c" opacity=".5"/></svg>
      dana@yourwebsite.com
    </li>
    <li>
      <svg viewBox="0 0 16 16" aria-hidden="true"><path d="M8 1a7 7 0 1 0 0 14A7 7 0 0 0 8 1zm0 1.5c.8 0 1.7 1.6 2 4H6c.3-2.4 1.2-4 2-4zM2.6 6.5h2c0-.9.2-2 .5-2.9A5.6 5.6 0 0 0 2.6 6.5zm8.8 0h2a5.6 5.6 0 0 0-2.5-2.9c.3.9.5 2 .5 2.9zM2.6 9.5a5.6 5.6 0 0 0 2.5 2.9c-.3-.9-.5-2-.5-2.9zm3.4 0c.3 2.4 1.2 4 2 4s1.7-1.6 2-4zm5.4 0c0 .9-.2 2-.5 2.9a5.6 5.6 0 0 0 2.5-2.9zM2.5 8h11"/></svg>
      www.yourwebsite.com
    </li>
  </ul>

  <div class="footer-band">SCRAP METAL RECYCLING</div>
</section>

</body>
</html>
```